Quorvane Capital Modern Business Card

We need a modern business card template designed for Quorvane Capital.
Quorvane Capital is a diversified global cryptocurrency investment fund.

The font under the logo: Hiragino Kaku Gothic Pro

Color Hexcode: Main colors white (ffffff) & teal (188383), we are open to adding #fcca46 as an accent

Target Market(s)

Accredited Investors, high net worth individuals and institutional investors

Industry/Entity Type

Investment

Contact Information for Business Card

Contact Information should contain
Name
main phone +1 720 555 0147
cell
email

Font styles to use
Sans Serif
Other font styles liked:
• Hiragino Kaku Gothic Pro

Requirements
Must have
• would like to have icons that identify the contact information
• include our website: www.quorvanecapital.example
• include our Tagline: Diversified Crypto Investment Funds
Nice to have
• Would like to have a simple back side with the logo (without the words) and plenty of space

```html
<!DOCTYPE html>
<html lang="en">
<head>
<meta charset="utf-8">
<title>Quorvane Capital Business Card</title>
<link rel="stylesheet" href="https://fonts.googleapis.com/css2?family=Poppins:wght@400;600&display=swap">
<style>
  :root {
    --teal: #239693;
    --yellow: #fcca46;
    --white: #ffffff;
    --page: #ffffff;
    --shadow: rgba(0, 0, 0, 0.16);
  }
  html, body {
    margin: 0;
    padding: 0;
    overflow: hidden;
    background: var(--page);
  }
  .canvas {
    position: relative;
    width: 1200px;
    height: 848px;
    overflow: hidden;
    background: var(--page);
    font-family: "Poppins", sans-serif;
  }
  .card {
    position: absolute;
    top: 256px;
    width: 522px;
    height: 338px;
    background: var(--white);
    box-shadow: 0 6px 12px var(--shadow);
  }
  .card--front { left: 64px; }
  .card--back { left: 614px; }

  .accent-panel {
    position: absolute;
    left: 164px;
    top: 25px;
    width: 335px;
    height: 288px;
    background: var(--yellow);
  }
  .brand-name {
    position: absolute;
    margin: 0;
    font-weight: 600;
    color: var(--teal);
    white-space: nowrap;
  }
  .card--front .brand-name {
    left: 40px;
    top: 244px;
    font-size: 23px;
    line-height: 1.15;
  }
  .brand-mark {
    position: absolute;
    left: 40px;
    top: 216px;
    width: 18px;
    height: 18px;
    background: var(--teal);
  }
  .holder {
    position: absolute;
    left: 301px;
    top: 245px;
    color: var(--teal);
  }
  .holder__name {
    margin: 0;
    font-size: 17px;
    font-weight: 600;
    line-height: 1.1;
  }
  .holder__role {
    margin: 0;
    font-size: 14px;
    font-weight: 400;
    line-height: 1.25;
  }

  .back-panel {
    position: absolute;
    left: 166px;
    top: 25px;
    width: 333px;
    height: 288px;
    background: var(--teal);
  }
  .card--back .brand-name {
    left: 30px;
    top: 56px;
    font-size: 13px;
    color: var(--white);
  }
  .tagline {
    position: absolute;
    left: 30px;
    top: 76px;
    margin: 0;
    font-size: 10px;
    font-weight: 400;
    color: var(--white);
    white-space: nowrap;
  }
  .contact-list {
    position: absolute;
    left: 30px;
    top: 170px;
    margin: 0;
    padding: 0;
    list-style: none;
    color: var(--white);
    font-size: 13px;
    line-height: 22px;
    white-space: nowrap;
  }
  .contact-list li {
    display: flex;
    align-items: center;
    gap: 9px;
  }
  .contact-list svg {
    width: 14px;
    height: 14px;
    fill: var(--white);
    flex: none;
  }
</style>
</head>
<body>
<main class="canvas">
  <section class="card card--front" aria-label="Card front">
    <div class="accent-panel"></div>
    <span class="brand-mark" aria-hidden="true"></span>
    <p class="brand-name">Quorvane Capital</p>
    <div class="holder">
      <p class="holder__name">JOHN DOE</p>
      <p class="holder__role">GENERAL MANAGER</p>
    </div>
  </section>

  <section class="card card--back" aria-label="Card back">
    <div class="back-panel">
      <p class="brand-name">QUORVANE CAPITAL</p>
      <p class="tagline">Diversified Crypto Investment Funds</p>
      <ul class="contact-list">
        <li>
          <svg viewBox="0 0 16 16" aria-hidden="true"><path d="M2 5c0-2 3-3 6-3s6 1 6 3v1h-3V5H5v1H2z"/><path d="M4 7h8l2 6H2z M8 8.5a2 2 0 1 0 0 4a2 2 0 0 0 0-4z"/></svg>
          <span>+1 720 555 0147</span>
        </li>
        <li>
          <svg viewBox="0 0 16 16" aria-hidden="true"><path d="M4.5 1h7a1 1 0 0 1 1 1v12a1 1 0 0 1-1 1h-7a1 1 0 0 1-1-1V2a1 1 0 0 1 1-1zM5 3v9h6V3zm3 10a.8.8 0 1 0 0 1.6A.8.8 0 0 0 8 13z"/></svg>
          <span>+1 720 555 0182</span>
        </li>
        <li>
          <svg viewBox="0 0 16 16" aria-hidden="true"><path d="M1 3h14v10H1zm1.5 1.5v.3L8 9l5.5-4.2v-.3zm0 2.2v4.8h11V6.7L8 10.9z"/></svg>
          <span>contact@quorvane-capital.example</span>
        </li>
        <li>
          <svg viewBox="0 0 16 16" aria-hidden="true"><path d="M8 1a7 7 0 1 0 0 14A7 7 0 0 0 8 1zm0 1.5a5.5 5.5 0 0 1 5.4 4.5H2.6A5.5 5.5 0 0 1 8 2.5zM2.6 9h10.8A5.5 5.5 0 0 1 2.6 9z"/></svg>
          <span>www.quorvanecapital.example</span>
        </li>
      </ul>
    </div>
  </section>
</main>
</body>
</html>
```